Redesign of company powerpoint

I would like to redesign the attached powerpoint. Can you modernize it for me? Feel free to change the orders of the powerpoint slide. It is a selling document during this Coronavirus crisis. Need to highlight we have invested significantly to automate and modernize our factory

Target Market(s)

Multinational electronic companies

Requirements
Must have
• Appear to conservative multinational PCB buyers. Convey a sense of confidence and trust in the presentation.

```html
<!DOCTYPE html>
<html lang="en">
<head>
<meta charset="utf-8">
<title>Norvale Circuits – Company Presentation</title>
<link href="https://fonts.googleapis.com/css2?family=Krona+One&family=Open+Sans:wght@400;600&family=Noto+Sans+SC:wght@400;500&display=swap" rel="stylesheet">
<style>
:root{
  --green:#0d4a22;
  --green-dark:#083818;
  --navy:#061627;
  --pcb:#0b4a6e;
  --pcb-deep:#03192b;
  --ink:#1d1d1d;
  --page:#e8e8e8;
  --white:#ffffff;
  --head:"Krona One",sans-serif;
  --body:"Open Sans","Noto Sans SC",sans-serif;
  --cjk:"Noto Sans SC",sans-serif;
}
*{box-sizing:border-box;margin:0;padding:0}
html,body{width:890px;height:1200px;overflow:hidden}
body{background:var(--page);position:relative;font-family:var(--body);color:var(--ink)}
.slide{position:absolute;width:392px;height:293px;background:var(--white);overflow:hidden;box-shadow:0 6px 10px rgba(0,0,0,.18)}
.slide--hero{left:219px;top:139px;width:452px;height:294px}
.slide--cover{left:34px;top:550px}
.slide--about{left:462px;top:550px}
.slide--intro{left:34px;top:870px}
.slide--thanks{left:462px;top:870px}

.photo{position:absolute;left:0;right:0}
.photo--pcb{top:0;height:75%;background:radial-gradient(circle at 50% 40%,#2a86b5 0%,var(--pcb) 30%,var(--pcb-deep) 85%)}
.curve{position:absolute;inset:0;width:100%;height:100%}
.cover-title{position:absolute;left:0;right:0;text-align:center;color:var(--green)}
.cover-title__en{font-family:var(--head);font-size:13px;letter-spacing:.5px}
.cover-title__cn{font-family:var(--cjk);font-size:16px;margin-top:2px}
.slide--cover .cover-title{top:243px}
.slide--hero .cover-title{top:241px}
.slide--hero .cover-title__en{font-size:15px}
.slide--hero .cover-title__cn{font-size:17px}

.tab{position:absolute;top:0;left:50%;transform:translateX(-50%);width:190px;height:6px;background:#222;border-radius:0 0 6px 6px}
.about-head{position:absolute;top:0;left:0;right:0;height:44px;display:flex;align-items:center;justify-content:center;gap:4px;padding-top:4px}
.about-head__en{font-family:var(--head);font-size:14px}
.about-head__cn{font-family:var(--cjk);font-size:16px}
.photo--studio{top:44px;height:231px;background:radial-gradient(ellipse at 75% 45%,#1e3038 0%,#140d10 45%,#0a0708 100%)}
.seal{position:absolute;left:118px;top:84px;width:156px;height:156px;border-radius:50%;background:var(--white);border:9px solid var(--green-dark);display:flex;align-items:center;justify-content:center}
.wordmark{font-family:var(--head);color:var(--green);letter-spacing:1px}
.seal .wordmark{font-size:30px}

.intro-title{position:absolute;left:0;width:155px;top:117px;text-align:right;font-family:var(--head);font-size:11px;line-height:16px}
.intro-title span{display:block;font-family:var(--cjk);font-size:13px}
.intro-rule{position:absolute;left:170px;top:27px;width:1px;height:240px;background:var(--ink)}
.point{position:absolute;left:182px;width:200px;display:flex;gap:9px}
.point__num{flex:none;width:30px;height:30px;border-radius:50%;background:var(--green);color:var(--white);font-weight:600;font-size:15px;display:flex;align-items:center;justify-content:center}
.point__text{font-size:7.4px;line-height:9px;padding-top:4px}
.point__text p+p{margin-top:3px}
.checks{list-style:none;margin-top:3px}
.checks li{position:relative;padding-left:14px}
.checks svg{position:absolute;left:0;top:1px}
.intro-mark{position:absolute;left:12px;top:270px;font-size:10px}
.footer-bar{position:absolute;left:0;right:0;bottom:0;height:4px;background:#222}
.page-no{position:absolute;right:0;bottom:0;width:40px;height:14px;background:var(--green);color:var(--white);font-size:7px;font-weight:600;display:flex;align-items:center;justify-content:center;clip-path:polygon(18% 0,100% 0,100% 100%,0 100%)}

.photo--city{top:0;height:100%;background:linear-gradient(180deg,#03081a 0%,#0a1c48 50%,#0b2a66 70%,#05112e 100%)}
.thanks-title{position:absolute;top:12px;left:0;right:0;text-align:center;color:var(--white);display:flex;justify-content:center;align-items:center;gap:5px}
.thanks-title__en{font-family:var(--head);font-size:13px}
.thanks-title__cn{font-family:var(--cjk);font-size:15px}
.thanks-mark{position:absolute;top:155px;left:0;right:0;text-align:center;font-size:20px}
.contacts{position:absolute;top:200px;left:0;right:0;display:flex}
.contact{flex:1;text-align:center;font-size:6.8px;line-height:8.4px}
.contact:first-child{flex:0 0 181px}
.contact__head{display:inline-block;font-family:var(--head);color:var(--green);font-size:7.5px;padding:0 4px 1px;border-bottom:1px solid var(--green);margin-bottom:4px}
.contact__line{display:flex;justify-content:center;gap:3px;margin-top:3px}
.contact__line svg{flex:none;margin-top:0}
.contact-rule{position:absolute;left:181px;top:205px;width:1px;height:66px;background:#999}
</style>
</head>
<body>

<!-- Hero cover -->
<section class="slide slide--hero">
  <div class="photo photo--pcb" role="img" aria-label="Close-up of a blue printed circuit board with a processor chip at its centre"></div>
  <svg class="curve" viewBox="0 0 392 293" preserveAspectRatio="none" aria-hidden="true">
    <path d="M0,293 L0,250 C70,190 220,170 392,228 L392,293 Z" fill="#fff"/>
    <path d="M0,265 C60,205 200,165 392,226 L392,232 C220,180 80,195 0,250 Z" fill="#0d4a22"/>
  </svg>
  <div class="cover-title">
    <div class="cover-title__en">NORVALE CIRCUITS LIMITED</div>
    <div class="cover-title__cn">諾瓦電路（東莞）有限公司</div>
  </div>
</section>

<!-- Cover -->
<section class="slide slide--cover">
  <div class="photo photo--pcb" role="img" aria-label="Close-up of a blue printed circuit board with a processor chip at its centre"></div>
  <svg class="curve" viewBox="0 0 392 293" preserveAspectRatio="none" aria-hidden="true">
    <path d="M0,293 L0,250 C70,190 220,170 392,228 L392,293 Z" fill="#fff"/>
    <path d="M0,265 C60,205 200,165 392,226 L392,232 C220,180 80,195 0,250 Z" fill="#0d4a22"/>
  </svg>
  <div class="cover-title">
    <div class="cover-title__en">NORVALE CIRCUITS LIMITED</div>
    <div class="cover-title__cn">諾瓦電路（東莞）有限公司</div>
  </div>
</section>

<!-- About -->
<section class="slide slide--about">
  <div class="tab"></div>
  <div class="about-head"><span class="about-head__en">ABOUT NVC /</span><span class="about-head__cn">NVC简介</span></div>
  <div class="photo photo--studio" role="img" aria-label="Dimly lit electronics workbench with a laptop and equipment in the background"></div>
  <div class="seal"><span class="wordmark">NVC</span></div>
</section>

<!-- Introduction -->
<section class="slide slide--intro">
  <div class="tab"></div>
  <h2 class="intro-title">INTRODUCTION<br>TO NVC<span>NVC 简介</span></h2>
  <div class="intro-rule"></div>

  <div class="point" style="top:24px">
    <div class="point__num">1</div>
    <div class="point__text"><p>A Hong Kong company established in 2007.</p><p>公司成立于2007</p></div>
  </div>
  <div class="point" style="top:69px">
    <div class="point__num">2</div>
    <div class="point__text"><p>Specialized in manufacturing single sided PCB in its own factory in Dongguan, China</p><p>专一单面板生产商，拥有自己在东莞的工厂</p></div>
  </div>
  <div class="point" style="top:122px">
    <div class="point__num">3</div>
    <div class="point__text"><p>Through continuous upgrade and installation of automated machine, NVC is one of the most efficient single sided PCB factories in China.</p><p>通过不断提升自动化设备，NVC现在是中国内最高效率的单面板工厂之一</p></div>
  </div>
  <div class="point" style="top:193px">
    <div class="point__num">4</div>
    <div class="point__text">
      <p>Current manufacturing facility as follows:<br>现在生产基地如下：</p>
      <ul class="checks">
        <li><svg width="8" height="8" viewBox="0 0 8 8"><rect x=".5" y=".5" width="7" height="7" fill="none" stroke="#0d4a22"/><path d="M2 4l1.5 1.5L6.5 2" fill="none" stroke="#0d4a22"/></svg>Norvale Circuits (Dongguan) Limited 诺瓦电路（东莞）有限公司</li>
        <li><svg width="8" height="8" viewBox="0 0 8 8"><rect x=".5" y=".5" width="7" height="7" fill="none" stroke="#0d4a22"/><path d="M2 4l1.5 1.5L6.5 2" fill="none" stroke="#0d4a22"/></svg>Production capacity 每月产能:<br>110,000 square meters a months</li>
        <li><svg width="8" height="8" viewBox="0 0 8 8"><rect x=".5" y=".5" width="7" height="7" fill="none" stroke="#0d4a22"/><path d="M2 4l1.5 1.5L6.5 2" fill="none" stroke="#0d4a22"/></svg>110,000 平米<br>Employees 员工人数: &nbsp;154</li>
      </ul>
    </div>
  </div>

  <div class="intro-mark wordmark">NVC</div>
  <div class="footer-bar"></div>
  <div class="page-no">03</div>
</section>

<!-- Thank you -->
<section class="slide slide--thanks">
  <div class="photo photo--city" role="img" aria-label="City skyline at night with lit towers reflected in the harbour"></div>
  <div class="thanks-title"><span class="thanks-title__en">THANK YOU /</span><span class="thanks-title__cn">谢谢您的观看</span></div>
  <svg class="curve" viewBox="0 0 392 293" preserveAspectRatio="none" aria-hidden="true">
    <path d="M0,293 L0,205 C80,145 230,120 392,185 L392,293 Z" fill="#fff"/>
    <path d="M0,215 C70,150 210,118 392,182 L392,188 C220,128 80,150 0,202 Z" fill="#0d4a22"/>
  </svg>
  <div class="thanks-mark wordmark">NVC</div>
  <div class="contact-rule"></div>
  <div class="contacts">
    <div class="contact">
      <div class="contact__head">HONG KONG</div>
      <div class="contact__line"><svg width="6" height="9" viewBox="0 0 6 9"><path d="M3 0a3 3 0 0 1 3 3c0 2-3 6-3 6S0 5 0 3a3 3 0 0 1 3-3z" fill="#0d4a22"/><circle cx="3" cy="3" r="1" fill="#fff"/></svg><span>18/F Harbour Crest, 12 Kai Cheung Road,<br>Kowloon Bay, HONG KONG</span></div>
      <div class="contact__line"><svg width="8" height="8" viewBox="0 0 8 8"><path d="M1.5 0l1.6 1.8-.9 1.3a5 5 0 0 0 2.7 2.7l1.3-.9L8 6.5 6.6 8C3 8 0 5 0 1.4z" fill="#0d4a22"/></svg><span>+852-3000 1234</span></div>
      <div class="contact__line"><svg width="9" height="7" viewBox="0 0 9 7"><rect width="9" height="7" fill="#0d4a22"/><path d="M0 0l4.5 4L9 0" fill="none" stroke="#fff" stroke-width=".8"/></svg><span>sales@norvalecircuits.com</span></div>
    </div>
    <div class="contact">
      <div class="contact__head">CHINA</div>
      <div class="contact__line"><svg width="6" height="9" viewBox="0 0 6 9"><path d="M3 0a3 3 0 0 1 3 3c0 2-3 6-3 6S0 5 0 3a3 3 0 0 1 3-3z" fill="#0d4a22"/><circle cx="3" cy="3" r="1" fill="#fff"/></svg><span>8 Jinhe East Road, 26 Industrial Zone<br>Shijie Town, Dongguan,<br>Guangdong Province, China 523290</span></div>
      <div class="contact__line"><svg width="8" height="8" viewBox="0 0 8 8"><path d="M1.5 0l1.6 1.8-.9 1.3a5 5 0 0 0 2.7 2.7l1.3-.9L8 6.5 6.6 8C3 8 0 5 0 1.4z" fill="#0d4a22"/></svg><span>+86(769)8000 4321</span></div>
      <div class="contact__line"><svg width="9" height="7" viewBox="0 0 9 7"><rect width="9" height="7" fill="#0d4a22"/><path d="M0 0l4.5 4L9 0" fill="none" stroke="#fff" stroke-width=".8"/></svg><span>sales@norvalecircuits.com</span></div>
    </div>
  </div>
</section>

</body>
</html>
```